Crest Vigor Affiliate Program

We are CrestVigor.com, a growing fitness and wellness community.

As part of our promotional strategy we have a robust Affiliate Program for affiliates to refer customers to us in exchange for a commission payable on each purchase.

We want a highly attractive and enticing short brochure describing the benefits of joining our Affiliate Program. This will be sent to prospective Affiliates to help persuade them to join and promote our products.

Length should be one large landscape page (or two portrait pages opened, magazine style).

I have attached the required text and features that should be included in the design. Particular focus should be placed on the "Why Become a Crest Vigor Affiliate" section and listed reasons.

I have also attached a couple of brochures that I would like to influence the designs I receive. I like the styles and concepts used in these examples.
Updates

Target Market(s)

Males aged 20-35. Amateur and Professional Online Marketers

Industry/Entity Type

Landscape

Requirements
Must have
• Include our Logo (attached).

Very clean, modern use of fonts, text styles and colors.

Must be "web 2.0" style in terms of appearance and graphics to be used.

Absolutely no early 2000s style clipart must be included.
Nice to have
• Cool graphics visually representing the listed reasons "Why Become a Crest Vigor Affiliate"
Should not have
• No clipart.
No cursive fonts.

```html
<!DOCTYPE html>
<html lang="en">
<head>
<meta charset="utf-8">
<title>Crest Vigor Affiliate Program Brochure</title>
<link rel="stylesheet" href="https://fonts.googleapis.com/css2?family=Source+Sans+3:wght@400;500;600&display=swap">
<style>
  :root {
    --navy: #032b45;
    --navy-deep: #0b2c44;
    --sky-blue: #1a95d4;
    --heading-blue: #2aa1df;
    --white: #ffffff;
    --stage: #e6e8ea;
    --photo-light: #c9d3dc;
    --photo-mid: #8e9aa5;
    --photo-dark: #5d6a6e;
  }
  * { margin: 0; padding: 0; box-sizing: border-box; }
  html, body {
    width: 1200px; height: 809px; overflow: hidden;
    background: var(--stage);
    font-family: "Source Sans 3", sans-serif;
  }
  .brochure {
    position: absolute; left: 47px; top: 14px;
    width: 1105px; height: 780px;
    background: var(--navy);
    overflow: hidden;
    box-shadow: 0 4px 14px rgba(0,0,0,.25);
  }
  .brochure-shapes { position: absolute; inset: 0; }
  .brand-name {
    position: absolute; right: 18px; top: 6px;
    font-size: 66px; font-weight: 500; letter-spacing: -1.5px;
    color: var(--navy-deep); line-height: 1;
  }
  .section-heading {
    position: absolute;
    font-size: 23px; font-weight: 500; letter-spacing: .4px;
    color: var(--heading-blue); text-transform: uppercase;
  }
  .benefits-heading { left: 32px; top: 362px; }
  .about-heading { left: 578px; top: 362px; }
  .program-heading { left: 578px; top: 549px; }
  .benefit-list {
    position: absolute; left: 40px; top: 399px;
    list-style: none; color: var(--white);
    font-size: 17.5px; line-height: 22.4px;
  }
  .benefit-list li { position: relative; padding-left: 28px; }
  .benefit-list li::before {
    content: ""; position: absolute; left: 2px; top: 8px;
    width: 7px; height: 7px; border-radius: 50%;
    background: var(--heading-blue);
  }
  .body-copy {
    position: absolute; left: 574px; width: 500px;
    color: var(--white); font-size: 17.5px; line-height: 22.4px;
  }
  .about-copy { top: 398px; }
  .about-copy p + p { margin-top: 8px; }
  .program-copy { top: 582px; }
  .footer-text {
    position: absolute; color: var(--white);
    font-size: 14.5px; text-align: center; line-height: 20px;
  }
  .footer-terms { left: 0; width: 552px; top: 750px; }
  .footer-contact { left: 552px; width: 553px; top: 729px; }
</style>
</head>
<body>
<main class="brochure">
  <svg class="brochure-shapes" width="1105" height="780" viewBox="0 0 1105 780">
    <defs>
      <linearGradient id="photoTone" x1="0" y1="0" x2="0" y2="1">
        <stop offset="0" stop-color="var(--photo-light)"/>
        <stop offset=".55" stop-color="var(--photo-mid)"/>
        <stop offset="1" stop-color="var(--photo-dark)"/>
      </linearGradient>
    </defs>
    <rect role="img" aria-label="Photo of two women in workout clothes doing a partner push exercise on a rooftop above a city skyline"
          x="0" y="0" width="1105" height="360" fill="url(#photoTone)"/>
    <path d="M0,196 Q552,480 1105,196 L1105,780 L0,780 Z" fill="var(--sky-blue)"/>
    <path d="M0,222 Q552,500 1105,222 L1105,780 L0,780 Z" fill="var(--navy)"/>
    <line x1="552" y1="0" x2="552" y2="780" stroke="var(--white)" stroke-width="1.2" stroke-dasharray="6 5" opacity=".85"/>
    <path d="M0,738 L552,712 L1105,712 L1105,780 L0,780 Z" fill="var(--white)"/>
    <path d="M0,742 L552,717 L1105,717 L1105,780 L0,780 Z" fill="var(--sky-blue)"/>
    <line x1="552" y1="717" x2="552" y2="780" stroke="var(--white)" stroke-width="1.2" stroke-dasharray="6 5" opacity=".85"/>
  </svg>

  <div class="brand-name">crest vigor</div>

  <h2 class="section-heading benefits-heading">Why become a Crest Vigor affiliate</h2>
  <ul class="benefit-list">
    <li>Customer endorses tried-and-tested products</li>
    <li>Expertly crafted persuasive copy</li>
    <li>Continual conversion optimization</li>
    <li>75% plus commission rates</li>
    <li>Bonus commission rates for top affiliates</li>
    <li>Lifetime commissions on all eligible customer purchases</li>
    <li>Regular affiliate contests and high value prizes</li>
    <li>Unprecedented affiliate training site</li>
    <li>Ready to go promotional tools</li>
    <li>Cut and paste ready promotions</li>
    <li>Bespoke marketing tools for JV partners</li>
    <li>Dedicated affiliate support</li>
  </ul>

  <h2 class="section-heading about-heading">About Crest Vigor</h2>
  <div class="body-copy about-copy">
    <p>Crest Vigor is a New York headquartered fitness community. We are open 24/7 at CrestVigor.com</p>
    <p>Our customers benefit from products that focus on actionable changes and a community-driven approach to wellness that produce outstanding body transformations.</p>
  </div>

  <h2 class="section-heading program-heading">About our affiliate program</h2>
  <div class="body-copy program-copy">
    <p>Second only to how much we love our customers is our commitment to Affiliates. What this means for you as a Crest Vigor affiliate is happy customers, massive social proof and low refund rates. We bend over backwards to help our Affiliates promote, persuade and profit.</p>
  </div>

  <p class="footer-text footer-terms">Full terms and conditions at CrestAffiliates.com</p>
  <p class="footer-text footer-contact">410 Harbor Lane, Suite 8B, New York 10014<br>Email: affiliates@crestvigor.com&nbsp;&nbsp; Ph: 555 014 2290</p>
</main>
</body>
</html>
```